Laundromat wall mural with logo, wash steps and soap dish instructions

Hi,
I am building a new laundromat and want to design a large wall mural containing a few different sections. The first piece would be a large image of my logo "Suds Harbor Laundromat" with my new tag line under it "A better Place to Wash". The next section would be general washing instructions: (step1) load clothes, (step 2) load soap, (step 3) select cycle (step 4) present payment (Quarters, Credit Card or Fennix/trove pay) (Step 5) Press start. Please use the wave from the logo to encase each of these 5 steps. Also please use an emblem in each wave to show each sections action. Such as they did in one of the example files I attached to this brief. The Final section would be the design for the soap compartment, describing where it goes. Please place the title "Where does the soap go?" above this section. The whole wall section will be 40 feet wide and 5 feet tall. I would like each section to flow aesthetically into the other. Feel free to use the logos waves and colors to bring everything together. I have attached examples of other store designs that I have found. The design will be above the washers that are placed against the wall.
I also placed a design of the mural that I wasn't completely impressed with so I opened the project to more designers.

Please let me know what other info you need.

Bests

Target Market(s)

laundromat customers

Industry/Entity Type

Laundromat

Font styles to use
Sans Serif

Colors
0054AA
0677BA
7BADD7
CADEEF
E8F1F8

Requirements
Must have
• The wave from my logo continuously flowing around the side and bottom borders.

```html
<!DOCTYPE html>
<html lang="en">
<head>
<meta charset="utf-8">
<title>Suds Harbor Laundromat – Wall Mural</title>
<link href="https://fonts.googleapis.com/css2?family=Poppins:wght@400;600;800&family=Exo+2:ital,wght@1,900&display=swap" rel="stylesheet">
<style>
  :root{
    --navy:#0054AA;
    --blue:#0677BA;
    --bright:#1a8fd6;
    --sky:#7BADD7;
    --mist:#CADEEF;
    --ice:#E8F1F8;
    --white:#ffffff;
    --stage:#808080;
  }
  *{box-sizing:border-box;margin:0;padding:0}
  html,body{width:1200px;height:1117px;overflow:hidden;background:var(--stage)}
  body{font-family:"Poppins",sans-serif;position:relative}
  .mural{position:absolute;left:20px;top:486px;width:1160px;height:145px;overflow:hidden;background:linear-gradient(var(--ice),var(--white) 40%);box-shadow:0 4px 10px rgba(0,0,0,.3)}
  .mural__waves{position:absolute;inset:0}
  .brand{position:absolute;left:22px;top:40px;width:250px;text-align:center}
  .brand__name{font-weight:800;font-size:29px;line-height:1;color:var(--navy);letter-spacing:-.5px}
  .brand__sub{font-weight:800;font-size:13px;color:var(--navy);letter-spacing:3px;margin-top:3px}
  .step{position:absolute;top:14px;display:flex;align-items:center;gap:5px}
  .step__drop{width:30px;height:38px}
  .step__label{color:var(--blue);font-weight:800;line-height:1.05}
  .step__num{display:block;font-size:8px;color:var(--sky);letter-spacing:.3px}
  .step__title{display:block;font-size:13px}
  .step__note{display:block;font-size:4.5px;font-weight:600;color:var(--blue);margin-top:2px;width:72px;line-height:1.3}
  .tagline{position:absolute;left:282px;top:97px;font-family:"Exo 2",sans-serif;font-style:italic;font-weight:900;font-size:33px;color:var(--white);letter-spacing:.5px;text-shadow:2px 2px 0 var(--navy)}
  .soap-q{position:absolute;left:820px;top:2px;width:136px;height:136px;border-radius:50%;background:var(--blue);border:4px solid var(--mist);display:flex;flex-direction:column;justify-content:center;align-items:center;color:var(--white);text-align:center;line-height:1}
  .soap-q__bold{font-weight:800;font-size:19px}
  .soap-q__light{font-weight:400;font-size:19px;margin:2px 0}
  .dispenser{position:absolute;left:1015px;top:6px;width:80px;height:110px;border-radius:4px;background:linear-gradient(#5b5b5b,#9a9a9a 60%,#e3e3e3)}
  .slot{position:absolute;display:flex;flex-direction:column;align-items:center;width:54px}
  .slot__label{font-size:4.5px;font-weight:800;color:var(--navy);text-align:center;line-height:1.2;margin-bottom:2px}
  .slot__icon{width:26px;height:26px;border-radius:50%;background:var(--blue);border:2px solid var(--mist)}
</style>
</head>
<body>
  <section class="mural" aria-label="Suds Harbor Laundromat wall mural">
    <svg class="mural__waves" viewBox="0 0 1160 145" preserveAspectRatio="none" aria-hidden="true">
      <path d="M0 80 C70 150 200 145 290 110 C330 95 400 80 470 88 C600 100 700 70 820 78 L1160 85 L1160 145 L0 145Z" fill="var(--sky)"/>
      <path d="M0 92 C80 150 210 150 300 120 C360 100 420 92 480 96 C620 108 720 80 830 88 C950 96 1050 120 1160 100 L1160 145 L0 145Z" fill="var(--bright)"/>
      <path d="M0 0 L70 0 C40 15 10 25 0 40Z" fill="var(--blue)"/>
      <path d="M0 130 C120 145 220 125 290 100 C250 140 150 148 0 145Z" fill="var(--mist)"/>
      <path d="M950 145 C1020 120 1080 125 1160 95 L1160 145Z" fill="var(--mist)" opacity=".8"/>
      <ellipse cx="150" cy="70" rx="140" ry="55" fill="var(--white)"/>
    </svg>

    <div class="brand">
      <div class="brand__name">SUDS HARBOR</div>
      <div class="brand__sub">LAUNDROMAT</div>
    </div>

    <div class="step" style="left:279px">
      <svg class="step__drop" viewBox="0 0 30 38" aria-hidden="true"><path d="M15 2 C22 14 28 20 28 26 A13 12 0 0 1 2 26 C2 20 8 14 15 2Z" fill="var(--blue)"/><rect x="9" y="21" width="12" height="10" rx="1" fill="none" stroke="var(--white)" stroke-width="1.5"/></svg>
      <span class="step__label"><span class="step__num">STEP 1</span><span class="step__title">LOAD<br>CLOTHES</span></span>
    </div>
    <div class="step" style="left:397px">
      <svg class="step__drop" viewBox="0 0 30 38" aria-hidden="true"><path d="M15 2 C22 14 28 20 28 26 A13 12 0 0 1 2 26 C2 20 8 14 15 2Z" fill="var(--blue)"/><ellipse cx="15" cy="26" rx="7" ry="5" fill="none" stroke="var(--white)" stroke-width="1.5"/></svg>
      <span class="step__label"><span class="step__num">STEP 2</span><span class="step__title">LOAD<br>SOAP</span></span>
    </div>
    <div class="step" style="left:500px">
      <svg class="step__drop" viewBox="0 0 30 38" aria-hidden="true"><path d="M15 2 C22 14 28 20 28 26 A13 12 0 0 1 2 26 C2 20 8 14 15 2Z" fill="var(--blue)"/><path d="M9 25 A6 6 0 0 1 21 24 M21 28 A6 6 0 0 1 9 29" fill="none" stroke="var(--white)" stroke-width="1.5"/></svg>
      <span class="step__label"><span class="step__num">STEP 3</span><span class="step__title">SELECT<br>CYCLE</span></span>
    </div>
    <div class="step" style="left:610px">
      <svg class="step__drop" viewBox="0 0 30 38" aria-hidden="true"><path d="M15 2 C22 14 28 20 28 26 A13 12 0 0 1 2 26 C2 20 8 14 15 2Z" fill="var(--blue)"/><rect x="8" y="21" width="14" height="9" rx="1.5" fill="none" stroke="var(--white)" stroke-width="1.5"/><line x1="8" y1="24" x2="22" y2="24" stroke="var(--white)" stroke-width="1.5"/></svg>
      <span class="step__label"><span class="step__num">STEP 4</span><span class="step__title">PRESENT<br>PAYMENT</span><span class="step__note">QUARTERS, CREDIT CARD OR FENNIX/TROVE PAY</span></span>
    </div>
    <div class="step" style="left:730px">
      <svg class="step__drop" viewBox="0 0 30 38" aria-hidden="true"><path d="M15 2 C22 14 28 20 28 26 A13 12 0 0 1 2 26 C2 20 8 14 15 2Z" fill="var(--blue)"/><path d="M12 31 L12 20 A1.5 1.5 0 0 1 15 20 L15 25 L20 26 L19 31Z" fill="none" stroke="var(--white)" stroke-width="1.5"/></svg>
      <span class="step__label"><span class="step__num">STEP 5</span><span class="step__title">PRESS<br>START</span></span>
    </div>

    <div class="tagline">A BETTER PLACE TO WASH</div>

    <div class="soap-q">
      <span class="soap-q__bold">WHERE</span>
      <span class="soap-q__light">DOES THE</span>
      <span class="soap-q__bold">SOAP GO?</span>
    </div>

    <div class="dispenser" role="img" aria-label="Photo of the washer soap dispenser tray with compartments"></div>

    <div class="slot" style="left:978px;top:22px"><span class="slot__label">FABRIC<br>SOFTENER</span><span class="slot__icon"></span></div>
    <div class="slot" style="left:1093px;top:18px"><span class="slot__label">LIQUID ONLY<br>DETERGENT / BLEACH</span><span class="slot__icon"></span></div>
    <div class="slot" style="left:978px;top:78px"><span class="slot__label">DETERGENT</span><span class="slot__icon"></span></div>
    <div class="slot" style="left:1093px;top:78px"><span class="slot__label">DETERGENT</span><span class="slot__icon"></span></div>
  </section>
</body>
</html>
```